BRIM Outreach Partners Business Card Rebrand

Hello Designers! We are looking for help designing our new business card to go in conjunction with our company rebrand. Unfortunately, we have an event mid June that requires we get these printed ASAP (before our new website is launched.) We have a mostly complete Brand Book which I have uploaded to this request for your reference to company information, style, fonts. I've also enclosed our logo file in .eps & .jpg. Attached is a sample business card my boss liked but said was "too simple." I made it in Canva and do not profess to be a designer. NOT FOR DESIGN REFERENCE, ONLY FOR CONTEXT Here is what our old website looks like: https://brimoutreachpartners.com/.

```html
<!DOCTYPE html>
<html lang="en">
<head>
<meta charset="utf-8">
<title>BRIM Outreach Partners — Business Card</title>
<link href="https://fonts.googleapis.com/css2?family=Poppins:wght@400;500;700&display=swap" rel="stylesheet">
<style>
  :root{
    --bg:#d9d9d9;
    --card-white:#ffffff;
    --card-grey:#ececec;
    --ink:#111111;
    --text:#2b2b2b;
    --blue:#4aaee0;
    --blue-light:#7cc7ec;
    --blue-deep:#3a9fd6;
  }
  *{box-sizing:border-box;margin:0;padding:0}
  html,body{width:1200px;height:1200px;overflow:hidden}
  body{background:var(--bg);font-family:"Poppins",sans-serif;position:relative}

  .card{position:absolute;left:180px;width:840px;height:480px;border-radius:28px;overflow:hidden;
        box-shadow:0 10px 28px rgba(0,0,0,.18)}
  .card-front{top:60px;background:var(--card-white)}
  .card-back{top:620px;background:linear-gradient(135deg,#f6f6f6,var(--card-grey))}

  .brand{position:absolute;display:flex;align-items:center;gap:22px}
  .brand-dot{border-radius:50%;background:linear-gradient(135deg,var(--blue-light),var(--blue))}
  .brand-name{font-family:"Poppins",sans-serif;font-weight:700;color:var(--ink);line-height:1.05}

  .card-front .brand{left:130px;top:120px}
  .card-front .brand-dot{width:150px;height:150px}
  .card-front .brand-name{font-size:46px;width:420px}

  .front-waves{position:absolute;inset:0}
  .socials{position:absolute;left:60px;bottom:26px;display:flex;align-items:center;gap:12px}
  .social-dot{width:26px;height:26px;border-radius:50%;background:#ffffff;opacity:.85}
  .handle{color:#fff;font-size:20px;font-weight:400;margin-left:12px}

  .card-back .brand{left:70px;top:60px;gap:16px}
  .card-back .brand-dot{width:100px;height:100px}
  .card-back .brand-name{font-size:32px;width:290px}

  .person{position:absolute;right:110px;top:118px;text-align:right}
  .person-name{font-weight:700;font-size:40px;color:var(--blue)}
  .person-role{font-size:18px;color:var(--text);margin-top:-4px}

  .edge{position:absolute;right:0;width:30px;background:var(--ink)}
  .edge-top{top:0;height:210px;border-bottom-left-radius:18px}
  .edge-tab{top:226px;height:60px;background:var(--blue);border-radius:14px 0 0 14px;width:40px}
  .edge-bottom{top:302px;height:178px;border-top-left-radius:18px}

  .contact{position:absolute;left:110px;top:290px;color:var(--text);font-size:19px}
  .address{line-height:1.35;margin-bottom:12px}
  .contact-row{display:flex;align-items:center;gap:14px;height:34px;font-size:21px}
  .contact-row svg{width:20px;height:20px;fill:var(--blue);flex:none}
</style>
</head>
<body>

<section class="card card-front">
  <svg class="front-waves" viewBox="0 0 840 480" preserveAspectRatio="none" aria-hidden="true">
    <defs>
      <linearGradient id="bandGrad" x1="0" x2="1" y1="0" y2="0">
        <stop offset="0" stop-color="#7cc7ec"/>
        <stop offset="1" stop-color="#3a9fd6"/>
      </linearGradient>
    </defs>
    <path d="M0 405 Q420 365 840 290 L840 480 L0 480 Z" fill="url(#bandGrad)"/>
    <path d="M330 392 C520 340 680 300 840 268 L840 300 C680 322 520 350 330 392 Z" fill="#111"/>
  </svg>
  <div class="brand">
    <span class="brand-dot"></span>
    <span class="brand-name">BRIM Outreach Partners</span>
  </div>
  <div class="socials">
    <span class="social-dot"></span>
    <span class="social-dot"></span>
    <span class="social-dot"></span>
    <span class="handle">@brim outreach partners</span>
  </div>
</section>

<section class="card card-back">
  <div class="brand">
    <span class="brand-dot"></span>
    <span class="brand-name">BRIM Outreach Partners</span>
  </div>

  <div class="person">
    <p class="person-name">Dana Whitfield</p>
    <p class="person-role">Attorney</p>
  </div>

  <div class="edge edge-top"></div>
  <div class="edge edge-tab"></div>
  <div class="edge edge-bottom"></div>

  <div class="contact">
    <p class="address">PO Box 51720, Nashville,<br>TN 37211</p>
    <p class="contact-row">
      <svg viewBox="0 0 24 24"><path d="M6.6 10.8a15 15 0 0 0 6.6 6.6l2.2-2.2c.3-.3.7-.4 1-.2 1.1.4 2.3.6 3.6.6.6 0 1 .4 1 1V20c0 .6-.4 1-1 1A17 17 0 0 1 3 4c0-.6.4-1 1-1h3.5c.6 0 1 .4 1 1 0 1.3.2 2.5.6 3.6.1.3 0 .7-.2 1z"/></svg>
      555-014-2290
    </p>
    <p class="contact-row">
      <svg viewBox="0 0 24 24"><path d="M2 5h20v14H2z M3 6l9 7 9-7" fill="none" stroke="#4aaee0" stroke-width="0"/><path d="M2 5h20v2l-10 7L2 7z"/><path d="M2 9l10 7 10-7v10H2z"/></svg>
      dana@brimoutreachpartners.com
    </p>
    <p class="contact-row">
      <svg viewBox="0 0 24 24"><circle cx="12" cy="12" r="10"/><path d="M2 12h20M12 2c3 3 3 17 0 20M12 2c-3 3-3 17 0 20" stroke="#fff" stroke-width="1.4" fill="none"/></svg>
      www.brimoutreachpartners.com
    </p>
  </div>
</section>

</body>
</html>
```